Creative - Appealing - Business Card Design Project

Looking for a Business card design (vector artwork) for an existing company called 'Fernway Sound'. We operate in the entertainment industry specializing in audio system design and rental, however; we also deal with other sectors of the entertainment industry including lighting, video, staging and power system design and rental. We would like to see designs that don't focus too much on audio but include elements encompassing everything else.

Double sided business card, following our new colour scheme and logo, which is attached. The card would ideally be creative and eye catching to draw in new customers in the elegant event production market, such as weddings & corporate affairs.

Target Market(s)

High end corporate clients, wedding clients

Industry/Entity Type

Entertainment

Requirements
Must have
• Our contact details, these can be worded & listed however you think appropriate as part as the design

Business Name - Fernway Sound
My Name - Dominic Harwell
Web Address - www.fernwaysound-example.com
Mobile Number - 07914 362 517
Office Number - 0330 481 7265
Email - dom@fernwaysound-example.com

The name, email and mobile number would need to be able to be changed to my business partners also.

The font used on our logo is Sansation
Nice to have
• On one side maybe a word cloud involving the services in which we can provide; Lighting, Sound, Event Production, Staging, LED Uplighting, Projection Mapping, Wedding Hire

On the other side, all the important credentials of contact.
Should not have
• The design should not use any old style fonts (i.e Times New Roman, Gothic etc) or on the other side of the scale, any 'jokey' fonts (i.e. Comic Sans).

The font to be used is Sansation

```html
<!DOCTYPE html>
<html lang="en">
<head>
<meta charset="utf-8">
<title>Fernway Sound – Business Card</title>
<link rel="stylesheet" href="https://fonts.googleapis.com/css2?family=Exo+2:wght@400;500;600;700&display=swap">
<style>
  :root {
    --stage: #1c1c1e;
    --card-dark: #2a292d;
    --card-mid: #4a4850;
    --glass: #b9b6c2;
    --violet: #6b4fa8;
    --violet-deep: #3b2a63;
    --violet-label: #7d62c4;
    --text-light: #eceaf1;
    --text-soft: #c9c6d1;
    --brand-grey: #d8d6dd;
  }
  * { margin: 0; padding: 0; box-sizing: border-box; }
  html, body { width: 1200px; height: 900px; overflow: hidden; }
  body {
    background: var(--stage);
    font-family: "Exo 2", "Helvetica Neue", Arial, sans-serif;
    color: var(--text-light);
    position: relative;
  }
  .card {
    position: absolute;
    left: 290px;
    width: 620px;
    height: 376px;
    overflow: hidden;
    border-radius: 4px;
    box-shadow: 0 14px 40px rgba(0,0,0,.55);
  }
  .card--contact { top: 50px; }
  .card--services { top: 474px; }
  .card__art { position: absolute; inset: 0; width: 100%; height: 100%; }

  /* Brand name lockup */
  .brand {
    position: absolute;
    display: flex;
    align-items: center;
    gap: 14px;
    font-weight: 600;
    color: var(--brand-grey);
    text-transform: uppercase;
    letter-spacing: .02em;
    line-height: 1;
  }
  .brand__dot {
    border-radius: 50%;
    background: var(--violet);
    flex: none;
  }
  .card--contact .brand { left: 44px; top: 250px; font-size: 38px; }
  .card--contact .brand__dot { width: 26px; height: 26px; }
  .card--services .brand { left: 70px; top: 118px; font-size: 50px; }
  .card--services .brand__dot { width: 34px; height: 34px; }

  /* Contact side */
  .contact {
    position: absolute;
    left: 330px;
    top: 92px;
  }
  .contact__name { font-size: 24px; font-weight: 500; margin-bottom: 12px; color: var(--text-light); }
  .contact__list { list-style: none; font-size: 13px; line-height: 1.45; }
  .contact__list li { display: flex; }
  .contact__label { width: 54px; color: var(--violet-label); }
  .contact__value { color: var(--text-soft); }
  .contact__web { margin-top: 18px; font-size: 17px; font-weight: 500; color: var(--text-light); }

  /* Services side */
  .tagline-url {
    position: absolute;
    left: 120px;
    top: 178px;
    font-size: 13px;
    letter-spacing: .34em;
    color: var(--text-soft);
  }
  .services {
    position: absolute;
    left: 40px;
    right: 40px;
    top: 238px;
    text-align: center;
    font-size: 17px;
    line-height: 1.5;
    color: var(--text-light);
  }
</style>
</head>
<body>

<section class="card card--contact" aria-label="Contact side of business card">
  <svg class="card__art" viewBox="0 0 620 376" preserveAspectRatio="none" aria-hidden="true">
    <defs>
      <linearGradient id="contactBase" x1="0" y1="0" x2="1" y2="1">
        <stop offset="0" stop-color="#3a393e"/>
        <stop offset=".55" stop-color="#2a292d"/>
        <stop offset="1" stop-color="#1f1e22"/>
      </linearGradient>
      <linearGradient id="contactGlass" x1="0" y1="0" x2="1" y2="0">
        <stop offset="0" stop-color="#cfcbd6" stop-opacity=".05"/>
        <stop offset=".6" stop-color="#cfcbd6" stop-opacity=".28"/>
        <stop offset="1" stop-color="#cfcbd6" stop-opacity=".5"/>
      </linearGradient>
      <linearGradient id="contactViolet" x1="0" y1="0" x2="1" y2="1">
        <stop offset="0" stop-color="#8a72c4" stop-opacity=".8"/>
        <stop offset="1" stop-color="#3b2a63" stop-opacity=".9"/>
      </linearGradient>
    </defs>
    <rect width="620" height="376" fill="url(#contactBase)"/>
    <polygon points="0,230 620,70 620,140 0,320" fill="url(#contactGlass)"/>
    <polygon points="420,0 620,0 620,120 520,60" fill="#d4d1da" fill-opacity=".35"/>
    <polygon points="470,0 560,0 620,230 620,290" fill="url(#contactViolet)" fill-opacity=".7"/>
    <polygon points="300,376 620,210 620,376" fill="#1a191d" fill-opacity=".75"/>
    <polygon points="60,376 620,250 620,270 140,376" fill="#6b4fa8" fill-opacity=".55"/>
  </svg>

  <div class="brand"><span class="brand__dot"></span>Fernway Sound</div>

  <div class="contact">
    <p class="contact__name">Dominic Harwell</p>
    <ul class="contact__list">
      <li><span class="contact__label">Mobile</span><span class="contact__value">07914 362 517</span></li>
      <li><span class="contact__label">Office</span><span class="contact__value">0330 481 7265</span></li>
      <li><span class="contact__label">Email</span><span class="contact__value">dom@fernwaysound-example.com</span></li>
    </ul>
    <p class="contact__web">www.fernwaysound-example.com</p>
  </div>
</section>

<section class="card card--services" aria-label="Services side of business card">
  <svg class="card__art" viewBox="0 0 620 376" preserveAspectRatio="none" aria-hidden="true">
    <defs>
      <linearGradient id="servicesBase" x1="0" y1="0" x2="1" y2="0">
        <stop offset="0" stop-color="#2b2433"/>
        <stop offset="1" stop-color="#3e3c44"/>
      </linearGradient>
      <linearGradient id="servicesGlass" x1="0" y1="0" x2="1" y2="1">
        <stop offset="0" stop-color="#e2dfe8" stop-opacity=".7"/>
        <stop offset="1" stop-color="#8d8a96" stop-opacity=".25"/>
      </linearGradient>
      <linearGradient id="servicesViolet" x1="0" y1="0" x2="1" y2="1">
        <stop offset="0" stop-color="#7a5cbd"/>
        <stop offset="1" stop-color="#3b2a63"/>
      </linearGradient>
    </defs>
    <rect width="620" height="376" fill="url(#servicesBase)"/>
    <polygon points="360,0 620,0 620,376 470,376" fill="url(#servicesGlass)"/>
    <polygon points="430,0 470,0 560,376 520,376" fill="#2a282e" fill-opacity=".8"/>
    <polygon points="500,0 520,0 620,260 620,330" fill="#2a282e" fill-opacity=".6"/>
    <polygon points="0,60 330,110 0,376" fill="url(#servicesViolet)" fill-opacity=".85"/>
    <polygon points="0,150 250,150 0,300" fill="#241c33" fill-opacity=".8"/>
    <polygon points="0,0 120,0 0,90" fill="#6b4fa8" fill-opacity=".55"/>
    <polygon points="0,376 0,330 300,376" fill="#1f1a27"/>
  </svg>

  <div class="brand"><span class="brand__dot"></span>Fernway Sound</div>
  <p class="tagline-url">www.fernwaysound-example.com</p>

  <p class="services">
    Lighting&nbsp; | &nbsp;Sound&nbsp; | &nbsp;Event Production&nbsp; | &nbsp;Staging&nbsp; | &nbsp;LED Uplighting<br>
    Projection Mapping&nbsp; | &nbsp;Wedding Hire
  </p>
</section>

</body>
</html>
```